Gardener needs an exciting new flyer design.

I'm a passionate gardener that requires a custom flyer design for a owner operator gardening business. Design will be for a DL flyer. I'm based on the Sunshine coast in Queensland Australia. My target audience is the residential market on the Sunshine coast. Business name is Marlowe Greens. My services are, lawn mowing, weeding, Eco Friendly fertilizing, green waste removal, Mulching, tree and shrub pruning, Full garden makeovers, hedging, pressure cleaning, privacy screening, Timber deck rejuvenation, Planting, Turf preparation and installation, and much more. Free no obligation quotes, reliable and friendly service, great rates. 12 years experience. Web www.marlowegreens.com.au - Phone 0418527064 - Email doug@marlowegreens.com.au I would like the design to portray a friendly and professional approach.

Target Market(s)

Residential

Industry/Entity Type

Gardener

Font styles to use
Serif

Colors
9ccb3b
abd037
3176b5

Requirements
Must have
• my services, my logo, my contact details,

```html
<!DOCTYPE html>
<html lang="en">
<head>
<meta charset="utf-8">
<title>Marlowe Greens – DL Flyer</title>
<link rel="stylesheet" href="https://fonts.googleapis.com/css2?family=PT+Sans:wght@400;700&display=swap">
<style>
  :root {
    --leaf-green: #3d8a3a;
    --panel-green: #357a38;
    --deep-green: #2c5a2a;
    --lime: #9ccb3b;
    --lime-soft: #abd037;
    --blue: #3176b5;
    --ribbon-blue: #3a9ee0;
    --plum: #6a2d7a;
    --white: #ffffff;
    --paper: #ffffff;
  }
  * { margin: 0; padding: 0; box-sizing: border-box; }
  html, body { width: 1200px; height: 2522px; overflow: hidden; background: var(--paper); }
  .flyer {
    position: relative;
    width: 1200px;
    height: 2522px;
    overflow: hidden;
    font-family: "PT Sans", "Myriad Pro", sans-serif;
    background: var(--paper);
  }
  .flyer-shapes { position: absolute; inset: 0; }

  .brand {
    position: absolute;
    top: 96px;
    left: 0;
    width: 1200px;
    display: flex;
    align-items: center;
    justify-content: center;
    gap: 36px;
  }
  .brand-dot {
    width: 104px; height: 104px;
    border-radius: 50%;
    background: var(--leaf-green);
    flex: none;
  }
  .brand-name {
    font-size: 112px;
    font-weight: 700;
    color: var(--leaf-green);
    line-height: 1;
  }

  .services {
    position: absolute;
    top: 268px;
    left: 90px;
    width: 1020px;
    text-align: center;
    color: var(--deep-green);
    font-size: 36px;
    line-height: 56px;
  }
  .services-title {
    display: block;
    font-weight: 700;
    color: var(--blue);
    font-size: 38px;
    letter-spacing: 3px;
    text-transform: uppercase;
    margin-bottom: 8px;
  }
  .services-sep { color: var(--lime); padding: 0 8px; }

  .intro {
    position: absolute;
    left: 97px;
    top: 1360px;
    width: 565px;
    color: var(--white);
    font-size: 40px;
    line-height: 50px;
  }
  .intro p + p { margin-top: 50px; }

  .contact {
    position: absolute;
    left: 0;
    width: 1200px;
    color: var(--white);
    display: flex;
    align-items: center;
    justify-content: center;
  }
  .contact-phone { top: 2276px; font-size: 76px; font-weight: 700; gap: 8px; line-height: 1; }
  .contact-web { top: 2372px; font-size: 56px; font-weight: 400; gap: 12px; line-height: 1; }
  .contact svg { flex: none; }
</style>
</head>
<body>
<div class="flyer">
  <svg class="flyer-shapes" width="1200" height="2522" viewBox="0 0 1200 2522">
    <defs>
      <linearGradient id="gardenTones" x1="0" y1="0" x2="0" y2="1">
        <stop offset="0" stop-color="#eef0ec"/>
        <stop offset="0.12" stop-color="#d6ddd0"/>
        <stop offset="0.3" stop-color="#5d8a45"/>
        <stop offset="0.55" stop-color="#3f6e2c"/>
        <stop offset="0.66" stop-color="#9c7a6e"/>
        <stop offset="0.74" stop-color="#5aa032"/>
        <stop offset="1" stop-color="#62b130"/>
      </linearGradient>
      <linearGradient id="pathTones" x1="0" y1="0" x2="0.3" y2="1">
        <stop offset="0" stop-color="#2f5e2a"/>
        <stop offset="0.3" stop-color="#4f7a3a"/>
        <stop offset="0.5" stop-color="#8a78b6"/>
        <stop offset="0.75" stop-color="#c7bfd2"/>
        <stop offset="1" stop-color="#a98cc0"/>
      </linearGradient>
      <linearGradient id="limeStripe" x1="0" y1="0" x2="1" y2="0">
        <stop offset="0" stop-color="#6fa83a"/>
        <stop offset="1" stop-color="#9ccb3b"/>
      </linearGradient>
    </defs>

    <polygon class="garden-photo" role="img" aria-label="Photo of a landscaped garden with a lawn, flower beds and tall trees"
             points="0,571 1200,571 1200,1180 0,1312" fill="url(#gardenTones)"/>
    <polygon class="accent-stripe" points="0,1312 1200,1176 1200,1262 0,1300" fill="url(#limeStripe)"/>

    <rect class="intro-panel" x="0" y="1294" width="694" height="912" fill="var(--panel-green)"/>
    <rect class="path-photo" role="img" aria-label="Photo of a stepping-stone garden path lined with lavender and flowers"
          x="698" y="1260" width="502" height="946" fill="url(#pathTones)"/>

    <polygon class="footer-band" points="0,2188 1200,2164 1200,2522 0,2522" fill="var(--deep-green)"/>

    <g class="experience-badge">
      <circle cx="968" cy="2078" r="106" fill="var(--plum)" stroke="var(--plum)" stroke-width="22" stroke-dasharray="12 10" stroke-linecap="round"/>
      <circle cx="968" cy="2078" r="88" fill="var(--blue)" stroke="var(--white)" stroke-width="5"/>
      <text x="968" y="2088" text-anchor="middle" fill="var(--white)" font-family="PT Sans, sans-serif" font-weight="700" font-size="82">12</text>
      <text x="968" y="2130" text-anchor="middle" fill="var(--white)" font-family="PT Sans, sans-serif" font-weight="700" font-size="36">YEARS</text>
      <polygon points="798,2144 1140,2144 1122,2173 1140,2202 798,2202 816,2173" fill="var(--ribbon-blue)"/>
      <text x="968" y="2187" text-anchor="middle" fill="var(--white)" font-family="PT Sans, sans-serif" font-weight="700" font-size="38">EXPERIENCE</text>
    </g>
  </svg>

  <div class="brand">
    <span class="brand-dot"></span>
    <span class="brand-name">Marlowe Greens</span>
  </div>

  <p class="services">
    <span class="services-title">Our Services</span>
    Lawn mowing<span class="services-sep">•</span>Weeding<span class="services-sep">•</span>Eco friendly fertilising<span class="services-sep">•</span>Mulching<br>
    Tree &amp; shrub pruning<span class="services-sep">•</span>Hedging<span class="services-sep">•</span>Green waste removal<br>
    Turf installation<span class="services-sep">•</span>Pressure cleaning<span class="services-sep">•</span>Free quotes
  </p>

  <div class="intro">
    <p>Marlowe Greens is your garden and lawn care specialist, with a passion for gardening and a keen eye for detail you can rest assured you're in the right hands.</p>
    <p>My services are tailored to meet every individual clients needs.</p>
    <p>From a one time mow too regular lawn mowing, all aspects of garden care and even full garden makeovers.</p>
  </div>

  <div class="contact contact-phone">
    <svg width="58" height="62" viewBox="0 0 24 24" aria-hidden="true">
      <path d="M6.6 10.8c1.4 2.8 3.8 5.1 6.6 6.6l2.2-2.2c.3-.3.7-.4 1-.2 1.1.4 2.3.6 3.6.6.6 0 1 .4 1 1V20c0 .6-.4 1-1 1C10.6 21 3 13.4 3 4c0-.6.4-1 1-1h3.5c.6 0 1 .4 1 1 0 1.3.2 2.5.6 3.6.1.3 0 .7-.2 1L6.6 10.8z" fill="var(--lime)"/>
    </svg>
    <span>0418527064</span>
  </div>

  <div class="contact contact-web">
    <svg width="56" height="56" viewBox="0 0 24 24" aria-hidden="true" fill="none" stroke="var(--lime)" stroke-width="1.6">
      <circle cx="12" cy="12" r="10"/>
      <ellipse cx="12" cy="12" rx="4.5" ry="10"/>
      <line x1="2" y1="12" x2="22" y2="12"/>
      <path d="M4 7h16M4 17h16"/>
    </svg>
    <span>www.marlowegreens.com.au</span>
  </div>
</div>
</body>
</html>
```